Wedding Invitation

We need a two cultural pieces put together in a wedding invitation. The colours are silver blue white. We are looking for light colours. The design should be light and breezy as possible as it is a beach wedding. The date for the wedding is March 21st 2014. Due to a breakdown in another designer we now find ourselves having to rush a design. We need the design in two days if possible of course.

Kind Regards
Helena Voskam

```html
<!DOCTYPE html>
<html lang="en">
<head>
<meta charset="utf-8">
<title>Wedding Invitation</title>
<link rel="stylesheet" href="https://fonts.googleapis.com/css2?family=Ubuntu+Condensed&family=Dancing+Script:wght@500&display=swap">
<style>
  :root {
    --page: #f5ead9;
    --card: #ffffff;
    --frame: #cde8ec;
    --panel: #d3ecef;
    --ornament: #c9e6ea;
    --pattern: #bfe2ea;
    --ink: #2b2b2b;
    --names: #2a3a7c;
  }
  * { margin: 0; padding: 0; box-sizing: border-box; }
  html, body { width: 1200px; height: 960px; overflow: hidden; }
  body { background: var(--page); position: relative; }

  .invitation {
    position: absolute; left: 378px; top: 14px;
    width: 444px; height: 934px;
    background: var(--card);
    box-shadow: 0 1px 4px rgba(0,0,0,0.12);
    overflow: hidden;
  }
  .arch-ornament {
    position: absolute; left: 30px; top: 31px; width: 386px; height: 100px;
    background: linear-gradient(180deg, #d9eef1, var(--ornament));
    border-radius: 60px 60px 0 0;
  }
  .frame-outer {
    position: absolute; left: 30px; top: 125px; width: 386px; height: 650px;
    background: var(--frame);
  }
  .frame-inner {
    position: absolute; left: 40px; top: 136px; width: 366px; height: 630px;
    background: var(--panel);
    border: 2px solid #ffffff;
    outline: 4px solid var(--panel);
    outline-offset: -8px;
  }
  .wording {
    position: absolute; left: 0; width: 444px; text-align: center;
    font-family: "Ubuntu Condensed", "Arial Narrow", sans-serif;
    font-size: 19px; line-height: 28px; color: var(--ink);
  }
  .verse { top: 158px; }
  .intro { top: 291px; }
  .invite { top: 498px; }
  .date { top: 579px; }
  .venue { top: 656px; }
  .date sup { font-size: 11px; vertical-align: 7px; line-height: 0; }

  .couple-name, .conjunction {
    position: absolute; left: 0; width: 444px; text-align: center;
    font-family: "Dancing Script", cursive; font-weight: 500;
    color: var(--names);
  }
  .couple-name { font-size: 44px; line-height: 56px; }
  .bride { top: 331px; }
  .groom { top: 418px; }
  .conjunction { top: 381px; font-size: 32px; line-height: 40px; }

  .tile-band {
    position: absolute; left: 0; top: 790px; width: 444px; height: 144px;
    background: linear-gradient(180deg, var(--pattern), #d0ebf1);
  }
</style>
</head>
<body>
  <main class="invitation">
    <div class="arch-ornament" role="img" aria-label="Light blue carved scroll arch ornament"></div>
    <div class="frame-outer"></div>
    <div class="frame-inner"></div>

    <p class="wording verse">As unique as a seashell<br>as deep as the sea<br>as eternal as the waves<br>our love is meant to be</p>
    <p class="wording intro">It is with joy that with our families we</p>

    <h1 class="couple-name bride">Caroline Puru</h1>
    <p class="conjunction">and</p>
    <h1 class="couple-name groom">Helena Voskam</h1>

    <p class="wording invite">invite you to share<br>our happiness on</p>
    <p class="wording date">Friday, 21<sup>st</sup> March 2014<br>at four in the afternoon at the</p>
    <p class="wording venue">Tidewater Resort<br>12 Seabreeze Street<br>Shellcove QLD</p>

    <div class="tile-band" role="img" aria-label="Pale blue geometric star tile pattern band"></div>
  </main>
</body>
</html>
```